Microsite (Mobile Landing Page)

A well-designed microsite with basic information about upcoming Quenmark mobile application, showing screens and explaining its features.

Target Market(s)

Android, iPhone and Tablet users

Requirements
Must have
• email subscription

Nice to have
• Have a look on this one:

http://www.plorvane.com/blog/images/2012/10/tundrel.png

```html
<!DOCTYPE html>
<html lang="en">
<head>
<meta charset="utf-8">
<title>Quenmark — Mobile App</title>
<link rel="stylesheet" href="https://fonts.googleapis.com/css2?family=Open+Sans:wght@400;600;700&display=swap">
<style>
:root{
  --green:#8cc640;
  --green-dark:#7fba35;
  --app-green:#9acd3a;
  --orange:#f26522;
  --orange-soft:#f7923a;
  --text-grey:#8a8a8a;
  --panel:#ffffff;
  --rule:#e6e6e6;
  --menu-bg:#3d3d3d;
  --menu-line:#484848;
  --phone:#141414;
  --dot:#4a4a4a;
}
*{margin:0;padding:0;box-sizing:border-box}
html,body{width:1200px;height:751px;overflow:hidden}
body{font-family:"Open Sans",Arial,sans-serif;background:linear-gradient(135deg,var(--green) 0%,var(--green-dark) 100%);position:relative}

.intro-panel{position:absolute;left:46px;top:0;width:366px;height:751px;background:var(--panel)}
.brand{position:absolute;left:52px;top:62px;display:flex;align-items:center;gap:8px}
.brand-square{width:54px;height:46px;background:var(--orange);border-radius:4px}
.brand-name{font-size:40px;font-weight:700;color:var(--app-green);letter-spacing:-1px;line-height:1}
.intro-title{position:absolute;left:52px;top:214px;font-size:18px;font-weight:600;color:var(--orange)}
.intro-text{position:absolute;left:52px;top:250px;width:290px;font-size:14.2px;line-height:22px;color:var(--text-grey)}
.subscribe{position:absolute;left:52px;top:392px;display:flex}
.subscribe-input{width:170px;height:28px;border:1px solid var(--rule);border-right:none;background:linear-gradient(#f3f3f3,#fff);font:inherit}
.subscribe-button{width:74px;height:28px;border:none;background:var(--orange);color:#fff;font:600 15px "Open Sans",Arial,sans-serif}
.footer{position:absolute;left:0;top:690px;width:366px;border-top:1px solid var(--rule);padding:20px 0 0 52px;font-size:12.5px;color:#777}
.footer a{color:#777;text-decoration:none}
.footer .sep{margin:0 8px}

.phone{position:absolute;left:471px;top:155px;width:359px;height:620px;background:var(--phone);border-radius:52px;border:3px solid #d8d8d8}
.phone-speaker{position:absolute;left:146px;top:56px;width:70px;height:14px;border-radius:7px;background:#555}
.phone-camera{position:absolute;left:107px;top:55px;width:16px;height:16px;border-radius:50%;background:#333}
.screen{position:absolute;left:20px;top:117px;width:314px;height:490px;background:#e9e9e9;overflow:hidden}
.app-bar{height:37px;background:var(--app-green);position:relative}
.app-bar-button{position:absolute;left:10px;top:8px;width:26px;height:20px;background:#fff;border-radius:3px}
.app-bar-button i{position:absolute;left:6px;width:14px;height:2px;background:var(--orange)}
.side-screen{position:absolute;left:0;top:37px;width:48px;bottom:0;background:#f4f4f4}
.side-tab{position:absolute;left:0;top:34px;width:32px;height:22px;background:var(--orange);color:#fff;font-size:9px;font-weight:700;line-height:22px;text-align:right;padding-right:4px}
.side-edit{position:absolute;left:0;width:32px;height:36px;background:#fff;border:1px solid #ddd;border-left:none}
.side-edit span{position:absolute;left:5px;top:9px;width:20px;height:17px;background:#555;border-radius:3px}
.menu{position:absolute;left:48px;top:37px;right:0;bottom:0;background:var(--menu-bg)}
.menu-search{margin:14px 20px 0 19px;height:22px;background:#fff;font-size:8px;color:#888;line-height:22px;padding-left:9px}
.menu-greeting{display:flex;align-items:center;gap:14px;margin:16px 0 0 19px;height:64px;font-size:11.5px;font-weight:700;color:#fff}
.menu-greeting em{font-style:normal;color:var(--app-green)}
.avatar{width:50px;height:41px;background:linear-gradient(#9bb8c8,#c99a7a)}
.menu-list{list-style:none;margin-top:6px}
.menu-item{display:flex;align-items:center;height:36px;border-top:1px solid var(--menu-line);padding-left:22px;font-size:10.5px;font-weight:700;color:#fff;position:relative}
.menu-item svg{width:18px;height:18px;margin-right:15px;fill:#fff}
.menu-item.is-active{background:var(--orange-soft)}
.menu-add{position:absolute;right:0;top:0;width:44px;height:36px;background:#fff;color:var(--orange);font-size:24px;line-height:34px;text-align:center;font-weight:700}

.callout-dot{position:absolute;left:783px;top:373px;width:12px;height:12px;border-radius:50%;background:var(--orange-soft)}
.callout-line{position:absolute;left:795px;top:378px;width:60px;height:1px;background:#fff}
.callout-icon{position:absolute;left:855px;top:364px;width:29px;height:31px;background:#444;color:#fff;font:italic 700 20px Georgia,serif;text-align:center;line-height:31px;border-radius:2px}
.feature-card{position:absolute;left:867px;top:322px;width:293px;height:127px;background:#fff;padding:18px 20px 0 51px}
.feature-title{font-size:14.5px;font-weight:600;color:var(--orange);margin-bottom:6px}
.feature-text{font-size:12.3px;line-height:17px;color:var(--text-grey)}
.pager{position:absolute;left:1176px;top:351px;list-style:none}
.pager li{width:12px;height:12px;border-radius:50%;background:var(--dot);margin-bottom:7.5px}
.pager li.is-current{background:var(--orange)}
</style>
</head>
<body>

<section class="intro-panel">
  <div class="brand"><span class="brand-square"></span><span class="brand-name">quenmark</span></div>
  <h1 class="intro-title">Lorem ipsum dolor sit ipsum</h1>
  <p class="intro-text">Lorem ipsum dolor sit ipsum Lorem ipsum dolor sit ipsum Lorem ipsum dolor sit ipsum Lorem ipsum dolor sit ipsum Lorem ipsum dolor.</p>
  <form class="subscribe">
    <input class="subscribe-input" type="email" aria-label="Email address">
    <button class="subscribe-button" type="submit">Submit</button>
  </form>
  <nav class="footer"><a href="#">About us</a><span class="sep">I</span><a href="#">Contact us</a><span class="sep">I</span><a href="#">Privacy Policy</a></nav>
</section>

<div class="phone">
  <span class="phone-camera"></span><span class="phone-speaker"></span>
  <div class="screen">
    <div class="app-bar"><span class="app-bar-button"><i style="top:6px"></i><i style="top:9px"></i><i style="top:12px"></i></span></div>
    <div class="side-screen">
      <div class="side-tab">ner</div>
      <div class="side-edit" style="top:96px"><span></span></div>
      <div class="side-edit" style="top:132px"><span></span></div>
      <div class="side-edit" style="top:220px"><span></span></div>
      <div class="side-edit" style="top:256px"><span></span></div>
      <div class="side-edit" style="top:292px"><span></span></div>
    </div>
    <div class="menu">
      <div class="menu-search">Add a new record</div>
      <div class="menu-greeting"><div class="avatar" role="img" aria-label="User profile photo"></div><span><em>Good Day,</em> Orvelan!</span></div>
      <ul class="menu-list">
        <li class="menu-item"><svg viewBox="0 0 18 18"><circle cx="9" cy="4" r="3"/><rect x="5" y="8" width="8" height="9" rx="3"/></svg>Health Map</li>
        <li class="menu-item"><svg viewBox="0 0 18 18"><circle cx="8" cy="3.5" r="3"/><rect x="4" y="8" width="9" height="9" rx="2"/></svg>Simulation</li>
        <li class="menu-item"><svg viewBox="0 0 18 18"><ellipse cx="7" cy="7" rx="6" ry="5"/><ellipse cx="12" cy="11" rx="5" ry="4"/></svg>Challenges</li>
        <li class="menu-item is-active"><svg viewBox="0 0 18 18"><rect x="2" y="2" width="14" height="14" rx="2"/></svg>Booklet<span class="menu-add">+</span></li>
        <li class="menu-item"><svg viewBox="0 0 18 18"><path d="M3 2h12v4a6 6 0 0 1-12 0z"/><rect x="7" y="11" width="4" height="3"/><rect x="5" y="14" width="8" height="2"/></svg>Trophies</li>
        <li class="menu-item"><svg viewBox="0 0 18 18"><rect x="1" y="1" width="4" height="4"/><rect x="7" y="1" width="4" height="4"/><rect x="13" y="1" width="4" height="4"/><rect x="1" y="7" width="4" height="4"/><rect x="7" y="7" width="4" height="4"/><rect x="13" y="7" width="4" height="4"/><rect x="1" y="13" width="4" height="4"/><rect x="7" y="13" width="4" height="4"/><rect x="13" y="13" width="4" height="4"/></svg>More</li>
      </ul>
    </div>
  </div>
</div>

<span class="callout-dot"></span><span class="callout-line"></span>
<article class="feature-card">
  <h2 class="feature-title">Lorem ipsum dolor sit ipsum</h2>
  <p class="feature-text">Lorem ipsum dolor sit ipsum Lorem ipsum dolor sit ipsum Lorem ipsum dolor sit ipsum Lorem ipsum dolor sit ipsum Lorem ipsum dolor.</p>
</article>
<span class="callout-icon">i</span>

<ul class="pager"><li class="is-current"></li><li></li><li></li><li></li></ul>

</body>
</html>
```